A website for Varnholt Limited

We need a new and modern website for our company. We are engineering consultants and contractors (EPC) in the oil and gas industry and building services industry.
What we do:
Engineering, procurement, construction
Automation (safety and process)
Non-destructive testing
Training
We have an existing website and the content can be referred from there since we are remaking the website
For more information visit Varnholt Limited Kenya

Coding

Number of Pages Required

1 page

```html
<!DOCTYPE html>
<html lang="en">
<head>
<meta charset="utf-8">
<title>Varnholt Limited | Engineering Consultants</title>
<link href="https://fonts.googleapis.com/css2?family=Oswald:wght@500;600;700&family=Poppins:wght@400;500;600;700&display=swap" rel="stylesheet">
<style>
:root{
  --orange:#e8552e;
  --orange-2:#f39150;
  --dark:#2f2f2f;
  --ink:#222;
  --text:#444;
  --muted:#777;
  --light:#f5f3f1;
  --white:#fff;
}
*{margin:0;padding:0;box-sizing:border-box}
html,body{width:1200px;height:3518px;overflow:hidden;background:var(--white)}
body{position:relative;font-family:'Poppins',sans-serif;color:var(--text)}
.abs{position:absolute}
.display{font-family:'Oswald',sans-serif;font-weight:700;color:var(--ink);text-transform:uppercase;letter-spacing:.5px}
.btn{position:absolute;display:flex;align-items:center;justify-content:center;font-family:'Poppins',sans-serif;font-weight:600;font-size:13px;text-transform:uppercase}
.btn-orange{background:linear-gradient(90deg,var(--orange),var(--orange-2));color:var(--white)}
.btn-outline{border:2px solid #666;color:var(--ink);background:var(--white)}
.fill{position:absolute}

/* header */
.brand{left:93px;top:11px;display:flex;align-items:center;gap:10px}
.brand-mark{width:72px;height:72px;border-radius:50%;border:3px solid var(--orange)}
.brand-name{font-size:21px;line-height:1.2;color:#8a8a8a;font-weight:400;text-transform:uppercase}
.topline{top:11px;font-size:14px;color:#555;display:flex;align-items:center;gap:6px}
.social-top{left:1021px;top:13px;display:flex;gap:13px}
.social-top span{width:12px;height:12px;border-radius:50%;background:#666;display:block}
.nav{left:410px;top:40px;width:790px;height:57px;background:var(--dark);clip-path:polygon(0 0,100% 0,100% 100%,24px 100%)}
.nav ul{list-style:none;display:flex;align-items:center;gap:16px;height:100%;padding-left:46px}
.nav li{color:var(--white);font-size:14px;font-weight:600;text-transform:uppercase}

/* hero */
.hero-img{left:498px;top:98px;width:702px;height:554px;background:linear-gradient(135deg,#f7f4ef 0%,#cfc6bb 45%,#8d8176 70%,#efe9e3 100%)}
.hero-rule{left:89px;top:265px;width:98px;height:2px;background:linear-gradient(90deg,var(--orange),#f4a07a)}
.hero-kicker{left:199px;top:247px;font-size:31px;font-weight:600}
.hero-title{left:89px;top:278px;font-size:78px;line-height:74px}
.hero-copy{left:89px;top:436px;width:340px;font-size:14.5px;line-height:20px;color:#555}

/* services */
.section-title{font-size:44px}
.arrow-btn{position:absolute;width:26px;height:26px;background:var(--dark);display:flex;align-items:center;justify-content:center}
.card{position:absolute;top:741px;width:221px;height:309px;background:var(--white);box-shadow:0 10px 30px rgba(0,0,0,.09)}
.card .fill{left:0;top:0;width:221px;height:178px}
.card h3{position:absolute;left:16px;top:189px;font-size:18px;font-family:'Oswald',sans-serif;font-weight:600;color:var(--ink);text-transform:uppercase}
.card p{position:absolute;left:16px;top:212px;width:200px;font-size:14px;line-height:20px;color:#555}
.card .more{position:absolute;left:16px;top:275px;font-family:'Oswald',sans-serif;font-size:12px;font-weight:600;color:var(--orange);text-transform:uppercase}

/* about */
.about-copy{left:711px;top:1351px;width:404px;font-size:14.5px;line-height:19.6px;color:#444}

/* stats */
.stat{position:absolute;top:1806px;width:160px;text-align:center}
.stat svg{display:block;margin:0 auto}
.stat .num{position:absolute;left:0;top:0;width:160px;height:148px;display:flex;align-items:center;justify-content:center;font-family:'Oswald',sans-serif;font-weight:600;font-size:34px;color:var(--ink)}
.stat h4{margin-top:14px;font-family:'Oswald',sans-serif;font-weight:600;font-size:18px;color:var(--ink);text-transform:uppercase}
.stat small{display:block;font-size:14px;color:#555}

/* testimonial */
.quote-mark{left:288px;top:2555px;font-family:'Oswald',sans-serif;font-size:300px;line-height:1;color:#f7e1d8}
.test-copy{left:180px;top:2757px;width:420px;font-size:15.5px;line-height:24px;color:#444}
.dots{left:180px;top:2938px;display:flex;gap:12px}
.dots span{width:36px;height:3px;background:#bbb;display:block}
.dots span.on{background:var(--orange)}

/* cta + footer */
.footer-band{left:0;top:3092px;width:1200px;height:426px;background:var(--dark)}
.cta{left:198px;top:3022px;width:805px;height:131px;background:linear-gradient(90deg,var(--orange),var(--orange-2))}
.cta h2{position:absolute;left:46px;top:42px;font-size:42px;color:var(--white)}
.cta .btn{left:605px;top:38px;width:147px;height:55px;background:var(--white);color:var(--ink);font-size:13px}
.f-brand{left:106px;top:3243px;display:flex;align-items:center;gap:10px}
.f-brand .brand-mark{width:84px;height:84px;border-color:var(--white)}
.f-brand .brand-name{color:var(--white);font-size:25px}
.f-social{left:153px;top:3354px;display:flex;gap:8px}
.f-social span{width:26px;height:26px;border-radius:50%;border:1px solid #777;display:block}
.f-head{top:3202px;font-family:'Oswald',sans-serif;font-weight:600;font-size:18px;color:var(--white)}
.f-links{left:368px;top:3242px;list-style:none}
.f-links li{font-size:12.5px;color:#ddd;line-height:24.6px}
.f-contact{left:541px;top:3242px;width:230px;font-size:12.5px;line-height:16px;color:#ddd}
.f-contact .row{position:relative;padding-left:22px;margin-bottom:10px}
.f-contact svg{position:absolute;left:0;top:2px}
.f-news{left:794px;top:3242px;width:210px;font-size:12.5px;line-height:16px;color:#ddd}
.f-input{left:794px;top:3298px;width:241px;height:40px;background:#444;display:flex;align-items:center;padding:0 16px;font-size:12.5px;color:#ddd;gap:10px}
.to-top{left:1121px;top:3397px;width:40px;height:40px;border-radius:50%;background:#a4432c;display:flex;align-items:center;justify-content:center}
.f-rule{left:93px;top:3469px;width:1010px;height:1px;background:#555}
.copyright{left:0;top:3484px;width:1200px;text-align:center;font-family:'Oswald',sans-serif;font-size:12.5px;color:#ddd}
</style>
</head>
<body>

<!-- Header -->
<div class="abs brand"><span class="brand-mark"></span><span class="brand-name">Varnholt<br>Limited</span></div>
<div class="abs topline" style="left:408px">
  <svg width="12" height="10" viewBox="0 0 12 10"><rect x="0.5" y="0.5" width="11" height="9" fill="none" stroke="#e8552e"/><path d="M0.5 0.5 6 5 11.5 0.5" fill="none" stroke="#e8552e"/></svg>
  info@varnholt.co.ke</div>
<div class="abs topline" style="left:613px">
  <svg width="12" height="12" viewBox="0 0 12 12"><path d="M2 1 4.5 1 5.5 3.5 4 4.5Q5 7 7.5 8L8.5 6.5 11 7.5 11 10Q10 11 8 11 1 8 1 2Q1 1 2 1Z" fill="#e8552e"/></svg>
  +254 700 418 362</div>
<div class="abs social-top"><span></span><span></span><span></span><span></span></div>
<nav class="abs nav">
  <ul>
    <li><svg width="14" height="13" viewBox="0 0 14 13"><path d="M7 0 14 6.5 12 6.5 12 13 8.5 13 8.5 9 5.5 9 5.5 13 2 13 2 6.5 0 6.5Z" fill="#fff"/></svg></li>
    <li>About Us</li><li>Servicer</li><li>What We Operate</li><li>Partners</li><li>Our Partners</li><li>Contact Us</li>
  </ul>
</nav>

<!-- Hero -->
<div class="fill hero-img" role="img" aria-label="Engineer in hard hat blended with an oil refinery skyline"></div>
<div class="abs hero-rule"></div>
<div class="abs display hero-kicker">We Are</div>
<h1 class="abs display hero-title">Engineering<br>Consultants</h1>
<p class="abs hero-copy">the oil and gas industry and building services industry.</p>
<div class="btn btn-orange" style="left:89px;top:487px;width:140px;height:45px">Learn More</div>
<div class="btn btn-outline" style="left:235px;top:487px;width:140px;height:45px">Get A Quote</div>

<!-- Services -->
<h2 class="abs display section-title" style="left:0;top:676px;width:1200px;text-align:center">Our Services</h2>
<div class="arrow-btn" style="left:103px;top:875px"><svg width="10" height="8" viewBox="0 0 10 8"><path d="M9 4H1M4 1 1 4 4 7" fill="none" stroke="#fff"/></svg></div>
<div class="arrow-btn" style="left:1072px;top:875px"><svg width="10" height="8" viewBox="0 0 10 8"><path d="M1 4H9M6 1 9 4 6 7" fill="none" stroke="#fff"/></svg></div>

<article class="card" style="left:142px">
  <div class="fill" role="img" aria-label="Engineers reviewing plans on site" style="background:linear-gradient(135deg,#b9a890,#6f6457)"></div>
  <h3>Engineering</h3><p>Lorem Ipsum is simply dummy text of the printing and typesetting industry.</p><span class="more">Read More</span>
</article>
<article class="card" style="left:374px">
  <div class="fill" role="img" aria-label="Procurement team with a building model" style="background:linear-gradient(135deg,#2e3a4a,#c9b36a)"></div>
  <h3>Procurement</h3><p>Lorem Ipsum is simply dummy text of the printing and typesetting industry.</p><span class="more">Read More</span>
</article>
<article class="card" style="left:606px">
  <div class="fill" role="img" aria-label="Construction worker with crane at sunset" style="background:linear-gradient(180deg,#7fa3c2,#c9a276)"></div>
  <h3>Construction</h3><p>Lorem Ipsum is simply dummy text of the printing and typesetting industry.</p><span class="more">Read More</span>
</article>
<article class="card" style="left:837px">
  <div class="fill" role="img" aria-label="Technician operating a robotic automation cell" style="background:linear-gradient(135deg,#2f8fd0,#2b3f5c)"></div>
  <h3>Automation</h3><p>Lorem Ipsum is simply dummy text of the printing and typesetting industry.</p><span class="more">Read More</span>
</article>

<!-- About -->
<div class="fill" role="img" aria-label="Smiling engineer in orange hard hat and safety vest" style="left:0;top:1078px;width:683px;height:615px;background:linear-gradient(90deg,#9c9c9c 0%,#d98a4c 40%,#e6e6e6 80%,#fff 100%)"></div>
<h2 class="abs display section-title" style="left:711px;top:1292px">About Varnholt</h2>
<div class="abs about-copy">
  <p>Varnholt undertakes Design, Supply, Installation and Commissioning of LPG and Petroleum systems including LPG Reticulated Systems (piped gas). We also do LPG tank revalidation and recertification.</p>
  <p>Our clients include: Oil companies (both multinationals and local), government agencies, manufacturing companies, agricultural institutions, and the building services industry.</p>
</div>
<div class="btn btn-orange" style="left:711px;top:1529px;width:140px;height:43px">Read More</div>

<!-- Stats -->
<svg width="0" height="0" style="position:absolute"><defs><linearGradient id="ring" x1="0" y1="0" x2="1" y2="1"><stop offset="0" stop-color="#e8552e"/><stop offset="1" stop-color="#f3a060"/></linearGradient></defs></svg>
<div class="stat" style="left:203px">
  <svg width="150" height="148" viewBox="0 0 150 148"><circle cx="75" cy="74" r="71" fill="none" stroke="#e8e8e8" stroke-width="5"/><circle cx="75" cy="74" r="71" fill="none" stroke="url(#ring)" stroke-width="5" stroke-dasharray="348 446" transform="rotate(-90 75 74)"/></svg>
  <div class="num">78%</div><h4>Project Done</h4><small>Varnholt</small>
</div>
<div class="stat" style="left:414px">
  <svg width="150" height="148" viewBox="0 0 150 148"><circle cx="75" cy="74" r="71" fill="none" stroke="#e8e8e8" stroke-width="5"/><circle cx="75" cy="74" r="71" fill="none" stroke="url(#ring)" stroke-width="5" stroke-dasharray="410 446" transform="rotate(-90 75 74)"/></svg>
  <div class="num">92%</div><h4>Happy Clients</h4><small>Varnholt</small>
</div>
<div class="stat" style="left:626px">
  <svg width="150" height="148" viewBox="0 0 150 148"><circle cx="75" cy="74" r="71" fill="none" stroke="#e8e8e8" stroke-width="5"/><circle cx="75" cy="74" r="71" fill="none" stroke="url(#ring)" stroke-width="5" stroke-dasharray="268 446" transform="rotate(-90 75 74)"/></svg>
  <div class="num">60%</div><h4>Completed Co.</h4><small>Varnholt</small>
</div>
<div class="stat" style="left:837px">
  <svg width="150" height="148" viewBox="0 0 150 148"><circle cx="75" cy="74" r="71" fill="none" stroke="#e8e8e8" stroke-width="5"/><circle cx="75" cy="74" r="71" fill="none" stroke="url(#ring)" stroke-width="5" stroke-dasharray="392 446" transform="rotate(-90 75 74)"/></svg>
  <div class="num">88%</div><h4>Country Cover</h4><small>Varnholt</small>
</div>

<!-- Our Work -->
<h2 class="abs display section-title" style="left:87px;top:2065px">Our Work</h2>
<div class="arrow-btn" style="left:1055px;top:2086px"><svg width="10" height="8" viewBox="0 0 10 8"><path d="M9 4H1M4 1 1 4 4 7" fill="none" stroke="#fff"/></svg></div>
<div class="arrow-btn" style="left:1085px;top:2086px"><svg width="10" height="8" viewBox="0 0 10 8"><path d="M1 4H9M6 1 9 4 6 7" fill="none" stroke="#fff"/></svg></div>
<div class="fill" role="img" aria-label="Three engineers in hard hats reviewing a tablet" style="left:90px;top:2135px;width:356px;height:356px;background:linear-gradient(160deg,#8a8f96,#e08a3a 70%,#5e5e5e)"></div>
<div class="fill" role="img" aria-label="Engineers studying drawings beside a building under construction" style="left:470px;top:2135px;width:356px;height:356px;background:linear-gradient(160deg,#c9ccd0,#e3b070 70%,#d9d9d9)"></div>
<div class="fill" role="img" aria-label="Engineer in orange hard hat reading plans" style="left:850px;top:2135px;width:350px;height:356px;background:linear-gradient(160deg,#9fb6cf,#a86848 60%,#444e5c)"></div>

<!-- Testimonial -->
<div class="abs quote-mark" aria-hidden="true">“</div>
<h2 class="abs display section-title" style="left:180px;top:2684px;font-size:42px">What Our Client Say</h2>
<p class="abs test-copy">Lorem Ipsum is simply dummy text of the printing and typesetting industry. Lorem Ipsum has been the industry's standard dummy text ever since...</p>
<div class="abs display" style="left:180px;top:2850px;font-size:18px;font-weight:600">Ravi Ochieng</div>
<svg class="abs" style="left:180px;top:2878px" width="90" height="16" viewBox="0 0 90 16">
  <g fill="#f0a52a">
    <path id="st" d="M8 0 10 5.5 16 6 11.5 9.8 13 16 8 12.6 3 16 4.5 9.8 0 6 6 5.5Z"/>
    <use href="#st" x="18"/><use href="#st" x="36"/><use href="#st" x="54"/><use href="#st" x="72"/>
  </g>
</svg>
<div class="abs dots"><span></span><span class="on"></span><span></span></div>
<div class="fill" style="left:657px;top:2873px;width:73px;height:37px;border-radius:37px 37px 0 0;background:linear-gradient(180deg,var(--orange-2),var(--orange))"></div>
<div class="fill" role="img" aria-label="Client in straw hat holding a phone" style="left:675px;top:2612px;width:346px;height:346px;border-radius:50%;background:radial-gradient(circle at 50% 60%,#f2f2f2 0%,#dfe5ea 45%,#cdd6de 100%)"></div>

<!-- CTA + Footer -->
<div class="fill footer-band"></div>
<div class="abs cta">
  <h2 class="display">Get In Touch With Us</h2>
  <div class="btn">Contact Us</div>
</div>

<div class="abs f-brand"><span class="brand-mark"></span><span class="brand-name">Varnholt<br>Limited</span></div>
<div class="abs f-social"><span></span><span></span><span></span><span></span></div>

<div class="abs f-head" style="left:367px">Quick Link</div>
<ul class="abs f-links">
  <li>Home</li><li>About Us</li><li>Servicer</li><li>What We Oper-</li><li>ate</li><li>partners</li><li>Our Partners</li>
</ul>

<div class="abs f-head" style="left:541px">Contact Us</div>
<div class="abs f-contact">
  <div class="row"><svg width="10" height="13" viewBox="0 0 10 13"><path d="M5 0C2 0 0 2.2 0 5 0 8.5 5 13 5 13S10 8.5 10 5C10 2.2 8 0 5 0Z" fill="#e8552e"/><circle cx="5" cy="5" r="2" fill="#2f2f2f"/></svg>Kelvin Plaza, Next to Riverside Centre, Athi, Suite 14, Lakeview Road</div>
  <div class="row"><svg width="12" height="12" viewBox="0 0 12 12"><path d="M2 1 4.5 1 5.5 3.5 4 4.5Q5 7 7.5 8L8.5 6.5 11 7.5 11 10Q10 11 8 11 1 8 1 2Q1 1 2 1Z" fill="#e8552e"/></svg>Cell<br>254 711 506 274<br>+254 700 418 362</div>
  <div class="row"><svg width="12" height="10" viewBox="0 0 12 10"><rect width="12" height="10" fill="#e8552e"/><path d="M0 0 6 5 12 0" fill="none" stroke="#2f2f2f"/></svg>Email<br>info@varnholt.co.ke</div>
</div>

<div class="abs f-head" style="left:794px">Newsletter</div>
<p class="abs f-news">Lorem Ipsum is simply dummy text of the printing ...</p>
<div class="abs f-input">
  <svg width="12" height="10" viewBox="0 0 12 10"><rect x="0.5" y="0.5" width="11" height="9" fill="none" stroke="#aaa"/><path d="M0.5 0.5 6 5 11.5 0.5" fill="none" stroke="#aaa"/></svg>
  <span style="flex:1">Enter email address</span>
  <svg width="14" height="14" viewBox="0 0 14 14"><path d="M14 0 0 6 5 8 7 14Z" fill="#e8552e"/></svg>
</div>

<div class="abs to-top"><svg width="10" height="7" viewBox="0 0 10 7"><path d="M1 6 5 2 9 6" fill="none" stroke="#fff" stroke-width="1.5"/></svg></div>
<div class="abs f-rule"></div>
<div class="abs copyright">© Copyright 2023 | All Right Reserveds</div>

</body>
</html>
```